Driftmoor Vertical Estates Council revised design

We need a logo for our email and letterhead design. We are a non-profit home owners association looking to look a little more professional. Attached is our current "logo" but it doesn't work well with letters or email. We would like to stay with the same concept.

Target Market(s)

Home owners, attorney, bankers, legislators

Industry/Entity Type

Non Profit

Font styles to use
Sans Serif

Colors

Designer to choose colors to be used in the design.

Requirements
Must have
• Company name: Driftmoor Vertical Estates Council
Nice to have
• This will always be on a while background (paper or email)

```html
<!DOCTYPE html>
<html lang="en">
<head>
<meta charset="utf-8">
<title>Driftmoor Vertical Estates Council — Stationery</title>
<link href="https://fonts.googleapis.com/css2?family=Questrial&family=Arimo:wght@400;700&display=swap" rel="stylesheet">
<style>
  :root {
    --backdrop: #dcdcdc;
    --paper: #f4f4f4;
    --paper-edge: #d2d2d2;
    --gold: #c8891c;
    --ink: #4a4a4a;
    --ink-soft: #6a6a6a;
    --mist: #9aa8a8;
  }
  * { margin: 0; padding: 0; box-sizing: border-box; }
  html, body { width: 1200px; height: 899px; overflow: hidden; background: var(--backdrop); }
  body { position: relative; font-family: "Questrial", sans-serif; color: var(--ink); }

  .sheet { position: absolute; background: var(--paper); border: 1px solid var(--paper-edge); }

  .wordmark { display: flex; align-items: center; gap: 5px; color: var(--gold); font-family: "Questrial", sans-serif; font-weight: 400; text-transform: uppercase; line-height: 1.15; }
  .wordmark .mark-dot { flex: none; border-radius: 50%; background: var(--mist); }

  .contact { font-family: "Arimo", sans-serif; color: var(--ink-soft); }
  .contact li { list-style: none; display: flex; align-items: center; }
  .contact svg { flex: none; fill: var(--gold); }

  /* Letterhead */
  .letterhead { left: 153px; top: 80px; width: 377px; height: 532px; }
  .letterhead .wordmark { position: absolute; left: 33px; top: 48px; font-size: 8.5px; letter-spacing: 0.6px; width: 150px; }
  .letterhead .wordmark .mark-dot { width: 9px; height: 9px; }
  .letterhead .contact-block { position: absolute; left: 269px; top: 32px; padding-left: 8px; border-left: 1px solid #c9c9c9; font-size: 5.4px; line-height: 7px; }
  .letterhead .contact ul { margin-top: 3px; }
  .letterhead .contact svg { width: 5px; height: 5px; margin-right: 5px; }
  .letter-body { position: absolute; left: 33px; top: 152px; width: 312px; }
  .greeting { font-size: 10px; margin-bottom: 16px; }
  .letter-body p { font-size: 5.3px; line-height: 8.2px; color: var(--ink-soft); margin-bottom: 8.2px; text-align: justify; }
  .sign-off { font-size: 5.3px; color: var(--ink-soft); margin-top: 14px; }
  .signature { margin-top: 12px; width: 68px; height: 24px; background: linear-gradient(90deg, rgba(200,137,28,.35), rgba(200,137,28,.12)); border-radius: 3px; }

  /* Folder */
  .folder { left: 564px; top: 48px; width: 445px; height: 565px; }
  .folder .spine { position: absolute; top: 0; bottom: 0; width: 1px; background: #cfcfcf; }
  .folder .wordmark { position: absolute; left: 93px; top: 268px; font-size: 26px; letter-spacing: 1.5px; width: 290px; gap: 12px; }
  .folder .wordmark .mark-dot { width: 24px; height: 24px; }

  /* Business cards */
  .card { left: 66px; width: 159px; height: 91px; }
  .card-front { top: 656px; }
  .card-front .wordmark { position: absolute; left: 37px; top: 32px; font-size: 8px; letter-spacing: .5px; width: 110px; }
  .card-front .wordmark .mark-dot { width: 8px; height: 8px; }
  .card-back { top: 762px; }
  .card-back .wordmark { position: absolute; left: 13px; top: 35px; font-size: 6px; letter-spacing: .4px; width: 80px; }
  .card-back .wordmark .mark-dot { width: 6px; height: 6px; }
  .card-back .divider { position: absolute; left: 85px; top: 22px; width: 1px; height: 52px; background: #cfcfcf; }
  .card-back .contact { position: absolute; left: 93px; top: 20px; font-size: 3.9px; line-height: 5px; }
  .card-back .name { font-family: "Arimo", sans-serif; font-weight: 700; color: var(--gold); font-size: 5.2px; }
  .card-back .role { font-weight: 700; color: var(--ink); font-size: 3.9px; margin-bottom: 3px; }
  .card-back .contact ul { margin-top: 3px; }
  .card-back .contact svg { width: 3.5px; height: 3.5px; margin-right: 3px; }

  /* Envelopes */
  .envelope-front { left: 242px; top: 656px; width: 436px; height: 198px; }
  .envelope-front .wordmark { position: absolute; left: 22px; top: 26px; font-size: 10px; letter-spacing: .7px; width: 150px; }
  .envelope-front .wordmark .mark-dot { width: 10px; height: 10px; }
  .envelope-front .return-address { position: absolute; left: 31px; top: 74px; font-family: "Arimo", sans-serif; font-size: 5.4px; line-height: 7px; color: var(--ink-soft); }
  .envelope-back { left: 700px; top: 654px; width: 436px; height: 198px; overflow: hidden; }
  .envelope-back .flap { position: absolute; left: 0; top: 0; }
  .envelope-back .wordmark { position: absolute; left: 176px; top: 26px; font-size: 6.5px; letter-spacing: .4px; width: 90px; }
  .envelope-back .wordmark .mark-dot { width: 6px; height: 6px; }
</style>
</head>
<body>

<svg width="0" height="0" style="position:absolute" aria-hidden="true">
  <symbol id="icon-phone" viewBox="0 0 10 10"><path d="M2 0.5 L3.6 0.5 L4.2 3 L3 3.8 Q4 6 6.2 7 L7 5.8 L9.5 6.4 L9.5 8 Q9.5 9.5 8 9.5 Q1 9 0.5 2 Q0.5 0.5 2 0.5Z"/></symbol>
  <symbol id="icon-mobile" viewBox="0 0 10 10"><path d="M2.5 0 H7.5 V10 H2.5Z M3.5 1 V8 H6.5 V1Z"/></symbol>
  <symbol id="icon-fax" viewBox="0 0 10 10"><path d="M2.5 0.5 H7.5 V3.5 H2.5Z M0.5 4 H9.5 V8 H8 V6.5 H2 V8 H0.5Z M2.5 7 H7.5 V9.5 H2.5Z"/></symbol>
  <symbol id="icon-mail" viewBox="0 0 10 10"><path d="M0.5 2 H9.5 V8 H0.5Z M1 2.4 L5 5.4 L9 2.4" /></symbol>
  <symbol id="icon-web" viewBox="0 0 10 10"><circle cx="5" cy="5" r="4.5"/></symbol>
</svg>

<!-- Letterhead -->
<section class="sheet letterhead">
  <div class="wordmark"><span class="mark-dot"></span><span>Driftmoor Vertical Estates Council</span></div>
  <div class="contact contact-block">
    <address style="font-style:normal">4120 Larkspur Row<br>Fairbanks, Alaska 99712</address>
    <ul>
      <li><svg><use href="#icon-phone"/></svg>907 214 3380</li>
      <li><svg><use href="#icon-mobile"/></svg>907 518 2247</li>
      <li><svg><use href="#icon-fax"/></svg>907 214 3391</li>
      <li><svg><use href="#icon-mail"/></svg>office@driftmoor.org</li>
      <li><svg><use href="#icon-web"/></svg>www.driftmoor.org</li>
    </ul>
  </div>
  <div class="letter-body">
    <p class="greeting">Dear Mr. Hollis,</p>
    <p>Lorem ipsum dolor sit amet, consectetur adipiscing elit. Donec orci purus, luctus vitae dignissim eu, iaculis sed purus. Vivamus faucibus, ipsum nec aliquet viverra, leo mauris condimentum ligula, sit amet sagittis enim ligula quis arcu. Nam egestas tortor id nisi porttitor mattis. In tortor ante, ultricies in suscipit a, tempus non massa. Vivamus et auctor mi. Fusce vel massa nulla. Phasellus nec eros mauris, et scelerisque orci.</p>
    <p>Donec malesuada orci vitae nulla accumsan porta a id massa. Quisque accumsan iaculis magna sit amet fringilla. Maecenas consequat, magna eget tincidunt semper, odio nibh rutrum mi, id feugiat ante nisi eu risus. Vestibulum nunc orci, rhoncus a placerat in, ultricies in mi. Cras mattis varius eros, vel fringilla nisi suscipit eget. Quisque scelerisque sagittis nulla at porttitor.</p>
    <p>Sed id augue vitae urna euismod commodo aliquet a quam. Pellentesque arcu velit, cursus et malesuada ut, consequat et diam. Nullam erat sem, rhoncus id ullamcorper vitae, rhoncus et arcu. In ultricies ultricies nulla, ut rutrum nisi iaculis at. Donec eu magna a metus ornare faucibus. Fusce aliquet faucibus ultricies. Morbi semper, est id tincidunt gravida, sem arcu adipiscing lacus, ac bibendum nulla leo eu purus. Quisque nec diam sed risus consectetur accumsan quis quis nibh. Vestibulum id purus lorem.</p>
    <p>It is a long established fact that a reader will be distracted by the readable content of a page when looking at its layout. The point of using Lorem Ipsum is that it has a more-or-less normal distribution of letters, as opposed to using 'Content here, content here', making it look like readable English. Many desktop publishing packages</p>
    <div class="sign-off">Sincerely,</div>
    <div class="signature" role="img" aria-label="Handwritten signature of Alden Marsh"></div>
  </div>
</section>

<!-- Presentation folder -->
<section class="sheet folder">
  <span class="spine" style="left:4px"></span>
  <span class="spine" style="left:14px"></span>
  <span class="spine" style="left:24px"></span>
  <div class="wordmark"><span class="mark-dot"></span><span>Driftmoor Vertical Estates Council</span></div>
</section>

<!-- Business card, front -->
<section class="sheet card card-front">
  <div class="wordmark"><span class="mark-dot"></span><span>Driftmoor Vertical Estates Council</span></div>
</section>

<!-- Business card, back -->
<section class="sheet card card-back">
  <div class="wordmark"><span class="mark-dot"></span><span>Driftmoor Vertical Estates Council</span></div>
  <span class="divider"></span>
  <div class="contact">
    <div class="name">ALDEN MARSH</div>
    <div class="role">CEO/FOUNDER</div>
    <address style="font-style:normal">4120 Larkspur Row<br>Fairbanks, Alaska 99712</address>
    <ul>
      <li><svg><use href="#icon-phone"/></svg>907 214 3380</li>
      <li><svg><use href="#icon-mobile"/></svg>907 518 2247</li>
      <li><svg><use href="#icon-fax"/></svg>907 214 3391</li>
      <li><svg><use href="#icon-mail"/></svg>office@driftmoor.org</li>
      <li><svg><use href="#icon-web"/></svg>www.driftmoor.org</li>
    </ul>
  </div>
</section>

<!-- Envelope, front -->
<section class="sheet envelope-front">
  <div class="wordmark"><span class="mark-dot"></span><span>Driftmoor Vertical Estates Council</span></div>
  <address class="return-address" style="font-style:normal">4120 Larkspur Row<br>Fairbanks, Alaska 99712</address>
</section>

<!-- Envelope, back -->
<section class="sheet envelope-back">
  <svg class="flap" width="436" height="62" viewBox="0 0 436 62" aria-hidden="true">
    <path d="M0 0 L10 46 Q14 60 30 60 L406 60 Q422 60 426 46 L436 0" fill="none" stroke="#cfcfcf" stroke-width="1"/>
  </svg>
  <div class="wordmark"><span class="mark-dot"></span><span>Driftmoor Vertical Estates Council</span></div>
</section>

</body>
</html>
```